Perky professional Bookkeeping Business card design needed

I need a business card for my new bookkeeping business. My target market is the owners of small businesses. I am a bright and bubbly young lady, not your typical accountant type and am looking for a bright, modern, perky yet professional card to reflect this.
I would like to use the symbol from framevault http://www.framevault.com/cat.mhtml?searchterm=business+wizard&search_group=&lang=en&search_source=search_form#id=60384915
as my logo but am open to colour schemes.
I want the design of the card to create confidence but not be too formal. Most people are scared of their bookkeepers/accountants and I want to be seen as approachable.
Target Market(s)
Business owners
Industry/Entity Type
Business
Contact Information for Business Card
Tally Spark Bookkeeping - image and name
Maren Holloway BBUS
Registered BAS AGENT 51730628
PO Box 738
Ashford Vale VIC 3961
Ph: 0437682915
Email: maren@tallysparkbookkeeping.com.au
Web: www.tallysparkbookkeeping.com.au
Tag line: Acheiving Maximum Results (not sure whether to include)
Look and feel

```html
<!DOCTYPE html>
<html lang="en">
<head>
<meta charset="utf-8">
<title>Tally Spark Bookkeeping – Business Card</title>
<link rel="stylesheet" href="https://fonts.googleapis.com/css2?family=Cinzel:wght@400;700&display=swap">
<style>
  :root {
    --stage-bg: #2f72b0;
    --stage-glow: #3f8fd0;
    --card-deep: #0d2f66;
    --card-mid: #1a4f93;
    --card-light: #3f8fd6;
    --panel: rgba(120, 170, 230, 0.22);
    --panel-edge: rgba(170, 205, 245, 0.25);
    --text-main: #ffffff;
    --text-soft: #d8e6f6;
  }
  * { box-sizing: border-box; margin: 0; padding: 0; }
  html, body { width: 950px; height: 1200px; overflow: hidden; }
  body {
    background: radial-gradient(ellipse at 50% 50%, var(--stage-glow) 0%, var(--stage-bg) 70%);
    font-family: 'Cinzel', Georgia, serif;
    color: var(--text-main);
    position: relative;
  }
  .card {
    position: absolute;
    left: 69px;
    width: 814px;
    height: 502px;
    overflow: hidden;
    box-shadow: 6px 8px 14px rgba(0, 0, 0, 0.45);
    background:
      radial-gradient(circle at 88% 62%, var(--card-light) 0%, var(--card-mid) 28%, transparent 55%),
      linear-gradient(135deg, var(--card-deep) 0%, var(--card-mid) 55%, var(--card-deep) 100%);
  }
  .card--front { top: 77px; }
  .card--back { top: 617px; }

  .brand-name {
    position: absolute;
    left: 0; right: 0;
    text-align center;
    text-align: center;
    font-weight: 700;
    font-size: 44px;
    line-height: 1;
    letter-spacing: 1px;
    color: var(--text-main);
  }
  .card--front .brand-name { top: 60px; }
  .card--back .brand-name { top: 240px; }

  .contact-panel {
    position: absolute;
    left: 0; top: 141px;
    width: 644px; height: 271px;
    background: var(--panel);
    border-top: 1px solid var(--panel-edge);
    box-shadow: 4px 6px 12px rgba(0, 0, 20, 0.35);
  }
  .person-name {
    position: absolute;
    left: 41px; top: 30px;
    font-size: 42px;
    font-weight: 400;
    letter-spacing: 1px;
  }
  .person-title {
    position: absolute;
    left: 41px; top: 86px;
    font-size: 18px;
    color: var(--text-soft);
  }
  .contact-list {
    position: absolute;
    left: 41px; top: 138px;
    list-style: none;
    font-size: 18px;
    color: var(--text-soft);
  }
  .contact-list li { display: flex; height: 32px; align-items: center; }
  .contact-label { width: 79px; }
  .contact-sep { width: 24px; }

  .postal-address {
    position: absolute;
    left: 0; right: 0; top: 466px;
    text-align: center;
    font-size: 16px;
    letter-spacing: 6px;
    color: var(--text-soft);
    padding-left: 60px;
  }
  .back-web {
    position: absolute;
    left: 0; right: 0; top: 296px;
    text-align: center;
    font-size: 18px;
    letter-spacing: 1px;
    color: var(--text-soft);
  }
</style>
</head>
<body>
  <section class="card card--front" aria-label="Business card front">
    <div class="brand-name">Tally Spark Bookkeeping</div>
    <div class="contact-panel">
      <h1 class="person-name">Maren Holloway</h1>
      <p class="person-title">BBUS Registered BAS AGENT 51730628</p>
      <ul class="contact-list">
        <li><span class="contact-label">Ph</span><span class="contact-sep">:</span><span>0437 682 915</span></li>
        <li><span class="contact-label">Email</span><span class="contact-sep">:</span><span>maren@tallysparkbookkeeping.com.au</span></li>
        <li><span class="contact-label">Web</span><span class="contact-sep">:</span><span>www.tallysparkbookkeeping.com.au</span></li>
      </ul>
    </div>
    <p class="postal-address">PO Box 738 Ashford Vale VIC 3961</p>
  </section>

  <section class="card card--back" aria-label="Business card back">
    <div class="brand-name">Tally Spark Bookkeeping</div>
    <p class="back-web">www.tallysparkbookkeeping.com.au</p>
  </section>
</body>
</html>
```